Mental Health Services for Employees - we need a website for our new business

We need a simple web design to showcase our various services. Our programs help organizations to ensure the heath and wellness of their workers. Our company is called "Harborline Workforce Solutions Inc." or "Harborline" We'd like to see designs that use the colour palette from our logo. Our customers our fairly conservative, and our design should communicate due diligence around providing a safe and healthy environment for workers. Attached our the logo files. Also sample photographs from our purchased images - others available. Original design for website is found here: https://pondlark7.sitebrook.example/page-1 A key page not listed in our original design is a section that lists "Five Reasons to Work With Us". We will need to be able to modify and change the copy/menu options as the business grows.

Target Market(s)

businesses who want to provide health and wellness services for their employees

Coding

Coded - Design and coding required

Number of Pages Required

2 page

Font styles to use
Sans Serif

Requirements
Must have
• colours that work with our attached logo

```html
<!DOCTYPE html>
<html lang="en">
<head>
<meta charset="utf-8">
<title>Harborline Workforce Solutions</title>
<link href="https://fonts.googleapis.com/css2?family=Lato:wght@400;700&family=Raleway:wght@500;600;700;800&display=swap" rel="stylesheet">
<style>
:root{
  --orange:#f7a823;
  --green:#1a9a78;
  --dark:#2b2b2b;
  --ink:#333;
  --muted:#555;
  --grey-bg:#f0f0f0;
  --white:#fff;
}
*{box-sizing:border-box;margin:0;padding:0}
html,body{width:1200px;height:4177px;overflow:hidden}
body{position:relative;font-family:'Lato',sans-serif;color:var(--ink);background:var(--white)}
.abs{position:absolute}
.head{font-family:'Raleway',sans-serif}

/* top bar */
.topbar{left:0;top:0;width:1200px;height:57px;background:var(--white);font-size:14px;color:#444}
.topbar .phone{left:113px;top:27px}
.topbar .mail{right:114px;top:27px}
.topbar svg{vertical-align:-2px;margin-right:6px}

/* hero */
.hero{left:0;top:57px;width:1200px;height:619px;background:linear-gradient(100deg,#5b5351 0%,#7e706a 35%,#9a958f 60%,#6f6d6e 100%)}
.brandbox{left:373px;top:0;width:431px;height:122px;background:var(--white);display:flex;align-items:center;justify-content:center;gap:14px;z-index:2}
.brandbox .mark{width:26px;height:26px;background:var(--orange)}
.brandbox .name{font-family:'Raleway',sans-serif;font-weight:700;font-size:30px;color:var(--dark)}
.nav{left:0;top:148px;width:1200px;display:flex;justify-content:center;gap:47px;font-family:'Raleway',sans-serif;font-size:16px;font-weight:500;color:var(--white);letter-spacing:.3px;padding-left:20px}
.hero-title{right:125px;top:290px;text-align:right;font-family:'Raleway',sans-serif;font-weight:600;font-size:36px;line-height:56px;color:var(--white)}
.arrow{width:48px;height:48px;border-radius:50%;display:flex;align-items:center;justify-content:center}
.arrow.light{background:var(--white)}
.arrow.solid{background:var(--orange)}

/* about */
.about-title{left:118px;top:765px;font-family:'Raleway',sans-serif;font-weight:800;font-size:40px;color:var(--dark)}
.about-text{left:118px;top:833px;width:459px;font-size:15px;line-height:31px;text-align:justify;color:#444}
.btn-more{left:120px;top:1091px;width:128px;height:39px;background:var(--orange);color:var(--white);border-radius:4px;font-size:14px;font-weight:700;display:flex;align-items:center;justify-content:center}
.about-photo{left:713px;top:819px;width:375px;height:285px;border-radius:60px 60px 0 60px;background:linear-gradient(160deg,#9bb7a6 0%,#d5b548 45%,#e5c43a 60%,#7e7d78 100%)}
.ring{border-radius:50%;border:2px solid #e6e6e6}
.dot{border-radius:50%;background:#e4e4e4}

/* services */
.services{left:0;top:1281px;width:1200px;height:584px;background:var(--grey-bg)}
.sec-title{width:1200px;left:0;text-align:center;font-family:'Raleway',sans-serif;font-weight:600;color:var(--dark)}
.card{width:292px;height:290px;border:4px solid var(--orange);border-radius:6px;padding:8px;background:var(--white)}
.card .ph{width:100%;height:100%;border-radius:4px}
.card-label{width:292px;text-align:center;font-family:'Raleway',sans-serif;font-weight:500;font-size:23px;line-height:27px;color:#555}

/* reasons */
.reasons{left:0;top:1865px;width:1200px;height:872px;background:linear-gradient(180deg,#fbf1ec 0%,#f8e6df 40%,#f0ded6 70%,#f2f0ef 100%)}
.reason-h{font-family:'Raleway',sans-serif;font-weight:600;font-size:22px;color:var(--green)}
.reason-p{font-size:11px;line-height:20px;color:#555}
.num{width:70px;height:70px;border-radius:50%;background:#cfcfcf;border:4px solid #3a3a3a;display:flex;align-items:center;justify-content:center;font-family:'Raleway',sans-serif;font-size:34px;font-weight:600;color:#333;box-shadow:0 0 0 3px #fff inset}
.num.active{background:var(--green);border-color:#fff;color:#fff;box-shadow:0 0 0 4px var(--green)}
.hub{left:475px;top:2157px;width:236px;height:236px;border-radius:50%;border:4px solid var(--orange);background:rgba(255,255,255,.55);display:flex;flex-direction:column;align-items:center;justify-content:center;gap:10px}
.hub .mark{width:24px;height:24px;background:var(--orange)}
.hub .name{font-family:'Raleway',sans-serif;font-weight:700;font-size:26px;color:var(--dark)}

/* gallery */
.gal{border-radius:0;box-shadow:0 8px 18px rgba(26,154,120,.18)}

/* footer */
.footer{left:0;top:3603px;width:1200px;height:513px;background:var(--dark)}
.foot-badge{left:525px;top:3534px;width:136px;height:136px;border-radius:50%;background:var(--white);border:2px dashed #333;display:flex;flex-direction:column;align-items:center;justify-content:center;gap:8px;z-index:2}
.foot-badge .mark{width:16px;height:16px;background:var(--orange)}
.foot-badge .name{font-family:'Raleway',sans-serif;font-weight:700;font-size:17px;color:var(--dark)}
.foot-title{font-family:'Raleway',sans-serif;font-weight:700;font-size:31px;color:var(--white)}
.field{left:115px;width:386px;border:2px solid #e8e8e8;color:#ddd;font-size:12px;padding:11px 14px;letter-spacing:.3px}
.btn-req{left:115px;top:4038px;width:191px;height:49px;background:var(--white);display:flex;align-items:center}
.btn-req span{flex:1;text-align:center;font-size:14px;font-weight:700;color:#333;padding-right:20px}
.btn-req .tip{width:56px;height:49px;background:var(--orange);clip-path:polygon(30% 0,100% 0,100% 100%,0 100%);display:flex;align-items:center;justify-content:center;padding-left:12px}
.contact-line{left:709px;font-size:15px;font-weight:700;color:var(--white);display:flex;align-items:center;gap:10px}
.social{left:713px;top:3940px;display:flex;gap:6px}
.social i{width:27px;height:27px;border-radius:50%;border:2px solid #eee;display:block}
.copy{left:0;top:4116px;width:1200px;height:61px;background:#1c1c1c;color:#eee;font-size:14px;padding:24px 0 0 111px}
</style>
</head>
<body>

<!-- header -->
<div class="abs topbar">
  <div class="abs phone"><svg width="13" height="13" viewBox="0 0 24 24"><path fill="#f7a823" d="M6.6 10.8a15 15 0 006.6 6.6l2.2-2.2c.3-.3.7-.4 1-.2 1.1.4 2.3.6 3.6.6.6 0 1 .4 1 1V20c0 .6-.4 1-1 1A17 17 0 013 4c0-.6.4-1 1-1h3.5c.6 0 1 .4 1 1 0 1.3.2 2.5.6 3.6.1.3 0 .7-.2 1z"/></svg>888-555-0142</div>
  <div class="abs mail"><svg width="14" height="11" viewBox="0 0 24 18"><path fill="#f7a823" d="M0 0h24v18H0z"/><path fill="none" stroke="#fff" stroke-width="2" d="M1 1l11 9 11-9"/></svg>coordinators@harborline-ws.example</div>
</div>

<div class="abs hero" role="img" aria-label="Photo of two colleagues in a calm workplace conversation"></div>
<div class="abs brandbox"><span class="mark"></span><span class="name">Harborline</span></div>
<nav class="abs nav"><span>HOME</span><span>SERVICES</span><span>ABOUT</span><span>SAP</span><span>REFERRALS</span><span>CONTACT</span><span>PORTAL</span></nav>
<h1 class="abs hero-title">HELPING ORGANIZATIONS<br>MAINTAIN A SAFE WORKPLACE</h1>
<div class="abs arrow light" style="left:49px;top:362px"><svg width="22" height="22" viewBox="0 0 24 24"><path fill="none" stroke="#f7a823" stroke-width="3" d="M20 12H5M11 5l-7 7 7 7"/></svg></div>
<div class="abs arrow light" style="left:1106px;top:362px"><svg width="22" height="22" viewBox="0 0 24 24"><path fill="none" stroke="#f7a823" stroke-width="3" d="M4 12h15M13 5l7 7-7 7"/></svg></div>

<!-- about -->
<div class="abs dot" style="left:498px;top:781px;width:52px;height:52px"></div>
<div class="abs dot" style="left:17px;top:992px;width:14px;height:14px"></div>
<div class="abs dot" style="left:54px;top:917px;width:50px;height:50px;background:#fde3e3"></div>
<div class="abs ring" style="left:101px;top:1124px;width:26px;height:26px"></div>
<div class="abs dot" style="left:968px;top:762px;width:15px;height:15px"></div>
<div class="abs ring" style="left:1098px;top:870px;width:56px;height:56px"></div>
<div class="abs ring" style="left:652px;top:1075px;width:28px;height:28px"></div>
<div class="abs ring" style="left:784px;top:1122px;width:28px;height:28px"></div>
<svg class="abs" style="left:715px;top:736px" width="165" height="85" viewBox="0 0 165 85"><polygon points="0,85 165,0 165,32 40,85" fill="#f9c46b"/></svg>
<svg class="abs" style="left:922px;top:1103px" width="165" height="83" viewBox="0 0 165 83"><polygon points="0,35 165,0 100,35 0,83" fill="#f9c46b"/></svg>

<h2 class="abs about-title">ABOUT US</h2>
<p class="abs about-text">Harborline Workforce Solutions Inc. (“Harborline”) provides outstanding business-to-business services that support and promote health, wellness, and safety in the workplace. Harborline’s flagship programs are the Substance Abuse Professional (SAP) and Specialized Addiction Case Management services. Harborline is ready to provide organizations with access to a suite of best-practice solutions and options for your employees.</p>
<div class="abs btn-more">Read More</div>
<div class="abs about-photo" role="img" aria-label="Photo of a yellow school bus driving on a highway"></div>

<svg class="abs" style="left:0;top:1214px" width="1200" height="68" viewBox="0 0 1200 68"><polygon points="0,0 560,67 0,67" fill="#1a9a78"/></svg>

<!-- services -->
<div class="abs services"></div>
<h2 class="abs sec-title" style="top:1357px;font-size:40px">SERVICES</h2>
<div class="abs card" style="left:104px;top:1437px"><div class="ph" role="img" aria-label="Photo of pilots at a cockpit control panel" style="background:linear-gradient(160deg,#2f3a33,#6e7a58 50%,#3b3f46)"></div></div>
<div class="abs card" style="left:452px;top:1437px"><div class="ph" role="img" aria-label="Photo of a worker wearing a safety harness" style="background:linear-gradient(160deg,#5a6278,#c48a62 50%,#d7c08a)"></div></div>
<div class="abs card" style="left:806px;top:1437px"><div class="ph" role="img" aria-label="Photo of a truck driver behind the wheel" style="background:linear-gradient(160deg,#9aa1a5,#6b5d4f 50%,#3e3f43)"></div></div>
<div class="abs card-label" style="left:104px;top:1749px">Accommodation<br>Screening</div>
<div class="abs card-label" style="left:452px;top:1752px">SAP<br>Assessments</div>
<div class="abs card-label" style="left:806px;top:1749px">Specialized Addiction<br>Case Management</div>

<!-- five reasons -->
<div class="abs reasons" role="img" aria-label="Faded background photo of a red locomotive at sunset"></div>
<svg class="abs" style="left:0;top:1865px" width="1200" height="66" viewBox="0 0 1200 66"><polygon points="640,0 1200,0 1200,65" fill="#1a9a78"/></svg>
<h2 class="abs sec-title" style="top:1972px;font-size:40px">Five Reasons to Work With Us</h2>

<svg class="abs" style="left:0;top:2100px" width="1200" height="460" viewBox="0 2100 1200 460" fill="none" stroke-width="2">
  <g stroke="#1a9a78"><line x1="425" y1="2170" x2="496" y2="2205"/></g>
  <g stroke="#222"><line x1="760" y1="2175" x2="690" y2="2205"/><line x1="425" y1="2370" x2="495" y2="2347"/><line x1="768" y1="2373" x2="690" y2="2347"/><line x1="591" y1="2393" x2="591" y2="2477"/></g>
  <g fill="#1a9a78"><circle cx="425" cy="2170" r="5"/><circle cx="496" cy="2205" r="5"/></g>
  <g fill="#222"><circle cx="760" cy="2175" r="5"/><circle cx="690" cy="2205" r="5"/><circle cx="425" cy="2370" r="5"/><circle cx="495" cy="2347" r="5"/><circle cx="768" cy="2373" r="5"/><circle cx="690" cy="2347" r="5"/><circle cx="591" cy="2393" r="5"/><circle cx="591" cy="2477" r="5"/></g>
</svg>
<div class="abs hub"><span class="mark"></span><span class="name">Harborline</span></div>
<div class="abs num active" style="left:351px;top:2114px">1</div>
<div class="abs num" style="left:769px;top:2118px">2</div>
<div class="abs num" style="left:348px;top:2342px">3</div>
<div class="abs num" style="left:784px;top:2345px">4</div>
<div class="abs num" style="left:558px;top:2491px">5</div>

<div class="abs" style="left:120px;top:2118px;width:210px;text-align:right"><div class="reason-h">Lorem Ipsum</div><div class="reason-p" style="margin-top:6px">Lorem ipsum dolor sit amet, consec-<br>tetur adipiscing elit, sed do</div></div>
<div class="abs" style="left:867px;top:2118px;width:220px"><div class="reason-h">Lorem Ipsum</div><div class="reason-p" style="margin-top:6px">Lorem ipsum dolor sit amet, consec-<br>tetur adipiscing elit, sed do</div></div>
<div class="abs" style="left:120px;top:2368px;width:210px;text-align:right"><div class="reason-h">Lorem Ipsum</div><div class="reason-p" style="margin-top:6px">Lorem ipsum dolor sit amet, consec-<br>tetur adipiscing elit, sed do</div></div>
<div class="abs" style="left:867px;top:2368px;width:220px"><div class="reason-h">Lorem Ipsum</div></div>
<div class="abs" style="left:450px;top:2583px;width:300px;text-align:center"><div class="reason-h">Lorem Ipsum</div><div class="reason-p" style="margin-top:6px">Lorem ipsum dolor sit amet, consec-<br>tetur adipiscing elit, sed do</div></div>

<!-- gallery -->
<h2 class="abs sec-title" style="top:2800px;font-size:40px">Gallery</h2>
<div class="abs gal" style="left:151px;top:2886px;width:282px;height:281px;background:linear-gradient(180deg,#c8cfd6,#8a7058 60%,#5a5550)" role="img" aria-label="Photo of a mining dump truck"></div>
<div class="abs gal" style="left:446px;top:2886px;width:308px;height:281px;background:linear-gradient(120deg,#4a4d52,#d9d6d2 45%,#a08a7c)" role="img" aria-label="Photo of a support agent wearing a headset"></div>
<div class="abs gal" style="left:764px;top:2886px;width:282px;height:281px;background:linear-gradient(180deg,#e89b7b,#b86a60 50%,#4c4a40)" role="img" aria-label="Photo of a red locomotive at sunset"></div>
<div class="abs gal" style="left:151px;top:3188px;width:360px;height:281px;background:linear-gradient(130deg,#6d6a6a,#d9b25c 40%,#d8a98e 70%,#cfc2b6)" role="img" aria-label="Photo of construction workers in hard hats"></div>
<div class="abs gal" style="left:532px;top:3188px;width:514px;height:281px;background:linear-gradient(120deg,#c9cfcf,#d7b49b 45%,#b8bdb6)" role="img" aria-label="Photo of a smiling family outdoors"></div>
<div class="abs arrow solid" style="left:49px;top:3153px"><svg width="22" height="22" viewBox="0 0 24 24"><path fill="none" stroke="#fff" stroke-width="3" d="M20 12H5M11 5l-7 7 7 7"/></svg></div>
<div class="abs arrow solid" style="left:1104px;top:3153px"><svg width="22" height="22" viewBox="0 0 24 24"><path fill="none" stroke="#fff" stroke-width="3" d="M4 12h15M13 5l7 7-7 7"/></svg></div>

<!-- footer -->
<div class="abs footer"></div>
<div class="abs foot-badge"><span class="mark"></span><span class="name">Harborline</span></div>
<h3 class="abs foot-title" style="left:113px;top:3670px">REQUEST A QUOTE</h3>
<div class="abs field" style="top:3749px;height:39px">FULL NAME</div>
<div class="abs field" style="top:3809px;height:39px">EMAIL ADDRESS</div>
<div class="abs field" style="top:3869px;height:39px">SUBJECT</div>
<div class="abs field" style="top:3929px;height:89px">MESSAGE</div>
<div class="abs btn-req"><span>REQUEST</span><div class="tip"><svg width="16" height="16" viewBox="0 0 24 24"><path fill="#fff" d="M2 11L22 2l-9 20-2-9z"/></svg></div></div>

<h3 class="abs foot-title" style="left:709px;top:3670px">CONTACT DETAILS</h3>
<div class="abs contact-line" style="top:3746px"><svg width="16" height="16" viewBox="0 0 24 24"><path fill="#f7a823" d="M2 11L22 2l-9 20-2-9z"/></svg>418 QUAYSIDE AVENUE, SUITE 300</div>
<div class="abs contact-line" style="top:3793px;left:737px">PORT ELDEN ONTARIO, L4X 2P7</div>
<div class="abs contact-line" style="top:3835px"><svg width="16" height="16" viewBox="0 0 24 24"><path fill="#f7a823" d="M6.6 10.8a15 15 0 006.6 6.6l2.2-2.2c.3-.3.7-.4 1-.2 1.1.4 2.3.6 3.6.6.6 0 1 .4 1 1V20c0 .6-.4 1-1 1A17 17 0 013 4c0-.6.4-1 1-1h3.5c.6 0 1 .4 1 1 0 1.3.2 2.5.6 3.6.1.3 0 .7-.2 1z"/></svg>PHONE: (007) 555 010 7890</div>
<div class="abs contact-line" style="top:3875px"><svg width="16" height="13" viewBox="0 0 24 18"><path fill="#f7a823" d="M0 0h24v18H0z"/><path fill="none" stroke="#2b2b2b" stroke-width="2" d="M1 1l11 9 11-9"/></svg>EMAIL: INQUIRY@QUILLMERE-TRANSIT.EXAMPLE</div>
<div class="abs social"><i></i><i></i><i></i><i></i></div>

<div class="abs copy">© Copyrights 2019. All rights reserved</div>

</body>
</html>
```